Real Estate Business Cards

Looking for a clean, sharp and professional look for our Real Estate investment Fund that invests in Multi Family Apartment buildings.

Target Market(s)

Real Estate Fund

Industry/Entity Type

Real Estate

Contact Information for Business Card

Company Description: Real Estate Investment Fund
Company Name: RKW Holdings
Name: Marcus Olvane
Cell: (917) 482-0657
Email: marcus@rkwholdings-example.com
Website: www.rkwholdings-example.com
Address: 418, 9th Street, Brooklyn NY 11218

Colors

Designer to choose colors to be used in the design.

Requirements
Nice to have
• Colors to match logo

```html
<!DOCTYPE html>
<html lang="en">
<head>
<meta charset="utf-8">
<title>RKW Holdings – Business Card</title>
<link rel="stylesheet" href="https://fonts.googleapis.com/css2?family=Lato:wght@400;700&display=swap">
<style>
  :root {
    --stage: #8c8c8c;
    --card: #231f20;
    --text: #f2f2f2;
    --accent: #5bb0e4;
    --icon: #e8e8e8;
  }
  * { box-sizing: border-box; margin: 0; padding: 0; }
  html, body {
    width: 1200px;
    height: 750px;
    overflow: hidden;
  }
  body {
    background: var(--stage);
    font-family: "Lato", Arial, sans-serif;
    color: var(--text);
    position: relative;
  }
  .card {
    position: absolute;
    top: 218px;
    width: 492px;
    height: 281px;
    background: var(--card);
  }
  .card--back { left: 100px; }
  .card--front { left: 601px; }

  .tagline {
    position: absolute;
    left: 123px;
    top: 127px;
    font-size: 18px;
    font-weight: 700;
    letter-spacing: 0.1px;
  }

  .brand {
    position: absolute;
    left: 140px;
    top: 64px;
    display: flex;
    align-items: center;
    gap: 10px;
  }
  .brand__square {
    width: 16px;
    height: 16px;
    background: var(--accent);
  }
  .brand__name {
    font-size: 24px;
    font-weight: 400;
    color: var(--text);
    letter-spacing: 0.5px;
  }

  .person {
    position: absolute;
    right: 20px;
    top: 86px;
    font-size: 19px;
    font-weight: 700;
    color: var(--accent);
  }

  .contact {
    position: absolute;
    right: 20px;
    top: 143px;
    list-style: none;
    text-align: right;
    font-size: 14px;
    line-height: 18px;
  }
  .contact li {
    display: flex;
    justify-content: flex-end;
    align-items: center;
    gap: 6px;
  }
  .contact svg {
    width: 14px;
    height: 12px;
    flex: none;
  }

  .address {
    position: absolute;
    left: 20px;
    top: 228px;
    font-style: normal;
    font-size: 14px;
    line-height: 16px;
  }
  .address__company { font-weight: 700; }
</style>
</head>
<body>
  <section class="card card--back" aria-label="Card back">
    <p class="tagline">Real Estate Investment Fund</p>
  </section>

  <section class="card card--front" aria-label="Card front">
    <div class="brand">
      <span class="brand__square"></span>
      <span class="brand__name">RKW Holdings</span>
    </div>

    <p class="person">Marcus Olvane</p>

    <ul class="contact">
      <li>(917) 482-0657
        <svg viewBox="0 0 14 12" aria-hidden="true"><rect x="4" y="0.5" width="6" height="11" rx="1" fill="none" stroke="var(--icon)"/><line x1="6" y1="9.5" x2="8" y2="9.5" stroke="var(--icon)"/></svg>
      </li>
      <li>marcus@rkwholdings-example.com
        <svg viewBox="0 0 14 12" aria-hidden="true"><rect x="0.5" y="2" width="13" height="8.5" fill="var(--icon)"/><polyline points="0.5,2 7,7 13.5,2" fill="none" stroke="var(--card)"/></svg>
      </li>
      <li>www.rkwholdings-example.com
        <svg viewBox="0 0 14 12" aria-hidden="true"><rect x="0.5" y="0.5" width="13" height="8.5" fill="none" stroke="var(--icon)"/><line x1="4" y1="11.5" x2="10" y2="11.5" stroke="var(--icon)"/><circle cx="7" cy="4.8" r="2" fill="none" stroke="var(--icon)"/></svg>
      </li>
    </ul>

    <address class="address">
      <span class="address__company">RKW Holdings</span><br>
      418, 9th Street, Brooklyn NY 11218
    </address>
  </section>
</body>
</html>
```